Talvo shoes is a wholesale shoe sales company , mostly working in female shoes and kiddies shoes with a small mens section . looking for a clean slick look. http://www.kemrafootwear.co.za/shop/ is a good reference

It Company

```html
<!DOCTYPE html>
<html lang="en">
<head>
<meta charset="utf-8">
<title>Talvo Shoes</title>
<link rel="stylesheet" href="https://fonts.googleapis.com/css2?family=Open+Sans:wght@400;600;700&family=Lato:wght@400;700;900&family=Roboto+Condensed:wght@400;700&display=swap">
<style>
  :root {
    --ink: #2b2b2b;
    --muted: #6d6d6d;
    --line: #e6e6e6;
    --topbar: #1f1f1f;
    --accent: #ef4a55;
    --paper: #ffffff;
    --band: #f8f6f6;
    --social: #8a9bb0;
    --card-chip: #d3d3d3;
    --suede: #5f3326;
    --suede-light: #7b4634;
    --denim: #26385a;
    --denim-light: #3a4f78;
  }
  * { box-sizing: border-box; margin: 0; padding: 0; }
  html, body { width: 734px; height: 1200px; overflow: hidden; background: var(--paper); }
  body { position: relative; font-family: "Open Sans", Arial, sans-serif; color: var(--ink); }
  .abs { position: absolute; }

  .top-bar { left: 0; top: 0; width: 734px; height: 20px; background: var(--topbar); }
  .account-links { right: 78px; top: 3px; font-size: 9px; color: #e9e9e9; letter-spacing: .1px; }
  .cart-pill { left: 665px; top: 2px; width: 28px; height: 16px; border: 1px solid #d9d9d9; border-radius: 8px; }
  .cart-pill svg { position: absolute; left: 7px; top: 2px; }

  .site-header { left: 0; top: 20px; width: 734px; height: 54px; border-bottom: 1px solid #f0f0f0; }
  .brand { left: 43px; top: 19px; font-weight: 700; font-size: 13px; letter-spacing: 1.5px; color: #3a3a3a; }
  .header-divider { left: 160px; top: 12px; width: 1px; height: 30px; background: var(--line); }
  .main-nav { top: 20px; font-size: 11.5px; color: var(--muted); }
  .social { top: 15px; width: 26px; height: 26px; border-radius: 50%; background: var(--social); }

  .hero { left: 43px; top: 91px; width: 650px; height: 284px; overflow: hidden;
    background:
      linear-gradient(180deg, rgba(238,232,224,.55) 0%, rgba(238,232,224,0) 38%, rgba(0,0,0,0) 62%, rgba(60,56,52,.35) 100%),
      linear-gradient(100deg, #cbbfb2 0%, #a69a8e 22%, #4a4440 48%, #2e2b2a 62%, #55504b 80%, #b5aca2 100%); }
  .hero-title { left: 15px; top: 78px; height: 42px; padding: 0 14px 0 15px; background: rgba(34,34,34,.9);
    font-family: "Lato", Arial, sans-serif; font-weight: 900; font-size: 29px; line-height: 42px; color: #fff; letter-spacing: .2px; }
  .hero-sub { left: 31px; top: 121px; font-family: "Lato", Arial, sans-serif; font-weight: 400; font-size: 14px; letter-spacing: 3.9px; color: #f2f2f2; }
  .hero-button { left: 33px; top: 163px; width: 141px; height: 34px; background: var(--accent); color: #fff;
    font-family: "Lato", Arial, sans-serif; font-weight: 700; font-size: 13px; line-height: 34px; text-align: center; }

  .section-title { left: 0; width: 734px; text-align: center; font-size: 13.5px; font-weight: 600; letter-spacing: 1px; color: #4a4a4a; }
  .section-rule { height: 1px; background: var(--line); }

  .product-card { width: 197px; height: 241px; border: 2px solid #efefef; background: var(--paper); }
  .product-photo { position: absolute; left: 34px; top: 20px; width: 127px; height: 154px; border-radius: 3px; }
  .photo-suede { background: linear-gradient(160deg, var(--suede-light) 0%, var(--suede) 55%, #4a271d 100%); }
  .photo-denim { background: linear-gradient(160deg, var(--denim-light) 0%, var(--denim) 55%, #1c2a45 100%); }
  .product-name { position: absolute; left: 0; top: 192px; width: 100%; text-align: center; font-size: 11.2px; color: #777; letter-spacing: .2px; }
  .product-price { position: absolute; left: 0; top: 210px; width: 100%; text-align: center; font-size: 12.5px; font-weight: 700; color: #444; }
  .product-price sup { font-size: 6.5px; vertical-align: 5px; font-weight: 600; }
  .sale-badge { position: absolute; left: -2px; top: 17px; width: 53px; height: 25px; background: var(--accent); color: #fff;
    font-size: 11.5px; font-weight: 700; line-height: 25px; text-align: center; }

  .signup-band { left: 0; top: 1054px; width: 734px; height: 72px; background: var(--band); }
  .signup-headline { left: 91px; top: 1077px; font-family: "Roboto Condensed", Arial, sans-serif; font-weight: 700; font-size: 11.8px; color: #222; }
  .signup-headline em { font-style: normal; color: var(--accent); }
  .signup-note { left: 144px; top: 1093px; font-family: "Roboto Condensed", Arial, sans-serif; font-size: 7.6px; color: #444; }
  .email-field { left: 364px; top: 1075px; width: 206px; height: 29px; background: #fff; border: 1px solid #ececec;
    font-size: 9.5px; color: #777; line-height: 27px; padding-left: 11px; }
  .signup-button { left: 591px; top: 1078px; width: 75px; height: 23px; background: var(--accent); color: #fff;
    font-family: "Roboto Condensed", Arial, sans-serif; font-size: 8.5px; line-height: 23px; text-align: center; }

  .footer-rule { left: 0; top: 1158px; width: 734px; height: 1px; background: #eeeeee; }
  .copyright { left: 43px; top: 1171px; font-size: 9px; color: #8a8a8a; }
  .pay-chip { top: 1171px; width: 22px; height: 12px; border-radius: 2px; background: var(--card-chip); }
</style>
</head>
<body>
  <div class="abs top-bar"></div>
  <div class="abs account-links">My Account :: My Cart :: Checkout :: Log In</div>
  <div class="abs cart-pill">
    <svg width="13" height="11" viewBox="0 0 13 11" aria-hidden="true">
      <path d="M0.5 1h2l1.5 6h7l1.3-4.5H3.2" fill="none" stroke="#e9e9e9" stroke-width="1.2"/>
      <circle cx="5" cy="9.3" r="1" fill="#e9e9e9"/><circle cx="10" cy="9.3" r="1" fill="#e9e9e9"/>
    </svg>
  </div>

  <header class="abs site-header">
    <div class="abs brand">TALVO SHOES</div>
    <div class="abs header-divider"></div>
    <nav>
      <span class="abs main-nav" style="left:186px">Men</span>
      <span class="abs main-nav" style="left:232px">Women</span>
      <span class="abs main-nav" style="left:294px">Kids</span>
      <span class="abs main-nav" style="left:340px">About Us</span>
      <span class="abs main-nav" style="left:407px">FAQs</span>
      <span class="abs main-nav" style="left:458px">Contact</span>
    </nav>
    <div class="abs social" style="left:635px"></div>
    <div class="abs social" style="left:665px"></div>
  </header>

  <section class="abs hero" role="img" aria-label="Fashion photo of a couple in evening wear crouching over luggage on a rooftop">
    <div class="abs hero-title">NEW SEASON ARRIVALS.</div>
    <div class="abs hero-sub">CHECK OUT ALL THE NEW TRENDS</div>
    <div class="abs hero-button">SHOP NOW</div>
  </section>

  <div class="abs section-rule" style="left:182px;top:422px;width:106px"></div>
  <div class="abs section-rule" style="left:446px;top:422px;width:108px"></div>
  <h2 class="abs section-title" style="top:412px">LATEST PRODUCTS</h2>

  <div class="abs product-card" style="left:44px;top:455px">
    <div class="product-photo photo-suede" role="img" aria-label="Brown suede high heel ankle boot"></div>
    <div class="product-name">LADIES HIGH HEEL ANKLE BOOTS</div>
    <div class="product-price">$150<sup>.00</sup></div>
  </div>
  <div class="abs product-card" style="left:269px;top:455px">
    <div class="product-photo photo-suede" role="img" aria-label="Brown suede high heel ankle boot"></div>
    <div class="sale-badge">-50%</div>
    <div class="product-name">LADIES HIGH HEEL ANKLE BOOTS</div>
    <div class="product-price">$650<sup>.00</sup></div>
  </div>
  <div class="abs product-card" style="left:496px;top:455px">
    <div class="product-photo photo-suede" role="img" aria-label="Brown suede high heel ankle boot"></div>
    <div class="product-name">LADIES HIGH HEEL ANKLE BOOTS</div>
    <div class="product-price">$100<sup>.00</sup></div>
  </div>

  <div class="abs section-rule" style="left:182px;top:743px;width:100px"></div>
  <div class="abs section-rule" style="left:452px;top:743px;width:102px"></div>
  <h2 class="abs section-title" style="top:733px">POPULAR PRODUCTS</h2>

  <div class="abs product-card" style="left:44px;top:775px">
    <div class="product-photo photo-denim" role="img" aria-label="Navy flat boot with brown buckle straps"></div>
    <div class="sale-badge">-86%</div>
    <div class="product-name">LADIES FLAT BOOTS WITH BUCKLES</div>
    <div class="product-price">$120<sup>.00</sup></div>
  </div>
  <div class="abs product-card" style="left:269px;top:775px">
    <div class="product-photo photo-denim" role="img" aria-label="Navy flat boot with brown buckle straps"></div>
    <div class="product-name">LADIES FLAT BOOTS WITH BUCKLES</div>
    <div class="product-price">$1000<sup>.00</sup></div>
  </div>
  <div class="abs product-card" style="left:496px;top:775px">
    <div class="product-photo photo-denim" role="img" aria-label="Navy flat boot with brown buckle straps"></div>
    <div class="product-name">LADIES FLAT BOOTS WITH BUCKLES</div>
    <div class="product-price">$340<sup>.00</sup></div>
  </div>

  <section class="abs signup-band"></section>
  <div class="abs signup-headline">SIGN UP NOW AND GET <em>10%</em> OFF YOUR FIRST ORDER</div>
  <div class="abs signup-note">RECIEVE EMAIL-EXCLUSIVE DEALS AND OTHER GREAT OFFERS</div>
  <div class="abs email-field">Email Address</div>
  <div class="abs signup-button">SIGN UP NOW</div>

  <div class="abs footer-rule"></div>
  <footer class="abs copyright">© 2014 Talvoshoes.com &nbsp;·&nbsp; All Rights Reserved</footer>
  <div class="abs pay-chip" style="left:569px"></div>
  <div class="abs pay-chip" style="left:603px"></div>
  <div class="abs pay-chip" style="left:637px"></div>
  <div class="abs pay-chip" style="left:672px"></div>
</body>
</html>
```